Letterhead for Law Firm Harborcrest Law Group

This would be for virtual letterhead, business cards, etc.

Also logo. I am happy to pay extra for that if it is a separate project.

Harborcrest Law Group

482 Larkmoor Avenue, Suite 730
San Francisco, California 94187

Target Market(s)

Business law services.

Industry/Entity Type

Business

Colors

Designer to choose colors to be used in the design.

```html
<!DOCTYPE html>
<html lang="en">
<head>
<meta charset="utf-8">
<title>Harborcrest Law Group – Identity Set</title>
<link rel="stylesheet" href="https://fonts.googleapis.com/css2?family=Arimo:wght@400;700&family=Jost:wght@400;500;600&display=swap">
<style>
  :root{
    --navy:#263673;
    --red:#b81f2a;
    --white:#ffffff;
    --board-light:#8b8b8b;
    --board-dark:#575757;
    --caption:#f2f2f2;
  }
  *{margin:0;padding:0;box-sizing:border-box}
  html,body{width:1200px;height:1000px;overflow:hidden}
  body{
    position:relative;
    background:linear-gradient(120deg,var(--board-light) 0%,#6d6d6d 50%,var(--board-dark) 100%);
    font-family:"Jost",sans-serif;
  }
  .brief{
    position:absolute;left:130px;top:83px;
    font-family:"Arimo",sans-serif;font-size:19px;line-height:24px;color:var(--caption);
  }
  .piece{position:absolute;overflow:hidden}
  .piece--white{background:var(--white)}
  .piece--navy{background:var(--navy)}

  .footer-band{position:absolute;left:0;bottom:0;width:100%;background:var(--navy)}
  .footer-rule{position:absolute;left:0;width:100%;background:var(--red)}

  .wordmark{
    position:absolute;left:0;width:100%;text-align:center;
    font-family:"Jost",sans-serif;font-weight:500;color:var(--navy);white-space:nowrap;
  }
  .wordmark--light{color:var(--white)}
  .mark-dot{position:absolute;border-radius:50%;background:var(--red)}

  .person{position:absolute;font-family:"Jost",sans-serif}
  .person__name{font-weight:600;font-size:13px;letter-spacing:.6px}
  .person__role{font-size:6.5px;margin-top:2px}
  .contacts{position:absolute;list-style:none;font-family:"Arimo",sans-serif;font-size:6.6px;line-height:8.8px}
  .contacts li{display:flex;align-items:flex-start}
  .contacts .ico{width:6px;height:6px;margin:1px 4px 0 0;flex:none;border-radius:1px}
  .on-navy{color:var(--white)}
  .on-navy .ico{background:var(--white)}
  .on-white{color:var(--navy)}
  .on-white .ico{background:var(--navy)}
</style>
</head>
<body>

<div class="brief">
  <p>Company Name: Harborcrest Law Group</p>
  <p>Logo design</p>
  <p>Business Card 2 front and 3 back Options</p>
  <p>Letterhead</p>
</div>

<!-- Logo panel -->
<section class="piece piece--white" style="left:130px;top:255px;width:335px;height:177px">
  <span class="mark-dot" style="left:155px;top:52px;width:26px;height:26px"></span>
  <div class="wordmark" style="top:120px;font-size:28px">Harborcrest Law Group</div>
</section>

<!-- Card front 1 (navy) -->
<section class="piece piece--navy" style="left:19px;top:473px;width:260px;height:152px">
  <div class="person on-navy" style="left:119px;top:14px">
    <div class="person__name">Marcus Ellery</div>
    <div class="person__role">CEO / Founder</div>
  </div>
  <ul class="contacts on-navy" style="left:119px;top:80px">
    <li><span class="ico"></span>+1 415.555.0173</li>
    <li><span class="ico"></span>+1 415.555.0173</li>
    <li><span class="ico"></span>office@harborcrestlaw.com</li>
    <li><span class="ico"></span>www.harborcrestlaw.com</li>
    <li><span class="ico"></span><span>482 Larkmoor Avenue, Suite 730<br>San Francisco, California 94187</span></li>
  </ul>
</section>

<!-- Card front 2 (white with footer band) -->
<section class="piece piece--white" style="left:297px;top:473px;width:262px;height:152px">
  <div class="person on-white" style="left:120px;top:16px">
    <div class="person__name">Marcus Ellery</div>
    <div class="person__role">CEO / Founder</div>
  </div>
  <ul class="contacts on-white" style="left:26px;top:67px">
    <li><span class="ico"></span>+1 415.555.0173</li>
    <li><span class="ico"></span>+1 415.555.0173</li>
    <li><span class="ico"></span>office@harborcrestlaw.com</li>
    <li><span class="ico"></span>www.harborcrestlaw.com</li>
    <li><span class="ico"></span><span>482 Larkmoor Avenue, Suite 730<br>San Francisco, California 94187</span></li>
  </ul>
  <span class="mark-dot" style="left:196px;top:70px;width:14px;height:14px"></span>
  <div class="wordmark" style="left:150px;width:106px;top:90px;font-size:11px">Harborcrest</div>
  <span class="footer-rule" style="bottom:14px;height:3px"></span>
  <span class="footer-band" style="height:10px"></span>
</section>

<!-- Card back 1 (white) -->
<section class="piece piece--white" style="left:19px;top:642px;width:261px;height:153px">
  <span class="mark-dot" style="left:120px;top:38px;width:20px;height:20px"></span>
  <div class="wordmark" style="top:98px;font-size:20px">Harborcrest Law Group</div>
</section>

<!-- Card back 2 (white with footer band) -->
<section class="piece piece--white" style="left:297px;top:642px;width:261px;height:152px">
  <span class="mark-dot" style="left:120px;top:34px;width:20px;height:20px"></span>
  <div class="wordmark" style="top:94px;font-size:20px">Harborcrest Law Group</div>
  <span class="footer-rule" style="bottom:14px;height:3px"></span>
  <span class="footer-band" style="height:10px"></span>
</section>

<!-- Card back 3 (navy) -->
<section class="piece piece--navy" style="left:19px;top:813px;width:260px;height:152px">
  <span class="mark-dot" style="left:120px;top:36px;width:20px;height:20px"></span>
  <div class="wordmark wordmark--light" style="top:94px;font-size:20px">Harborcrest Law Group</div>
</section>

<!-- Letterhead -->
<section class="piece piece--white" style="left:574px;top:165px;width:612px;height:792px">
  <span class="mark-dot" style="left:103px;top:32px;width:18px;height:18px"></span>
  <div class="wordmark" style="left:41px;width:auto;top:73px;font-size:19px">Harborcrest Law Group</div>

  <div style="position:absolute;right:151px;top:59px;text-align:right;font-family:'Arimo',sans-serif;font-weight:700;font-size:7.6px;line-height:9.5px;color:var(--navy)">
    482 Larkmoor Avenue, Suite 730<br>San Francisco, California 94187
  </div>
  <span style="position:absolute;left:468px;top:50px;width:1px;height:40px;background:var(--navy)"></span>
  <ul class="contacts on-white" style="left:474px;top:50px;font-size:7.4px;line-height:10.5px">
    <li><span class="ico"></span>+1 415.555.0173</li>
    <li><span class="ico"></span>+1 415.555.0173</li>
    <li><span class="ico"></span>office@harborcrestlaw.com</li>
    <li><span class="ico"></span>www.harborcrestlaw.com</li>
  </ul>

  <span class="footer-rule" style="bottom:36px;height:6px"></span>
  <span class="footer-band" style="height:28px"></span>
</section>

</body>
</html>
```